Moon Tot needs ecommerce website design help

We need someone to set up a fully functional website for us. We sell baby bibs, I attached them along with our company logo (MTG: moon tot goods). The bibs are made of 100% silicon, they are safe, light weight, soft, smooth, flexible, dishwasher safe and has funny faces.

Business name: Moon Tot Goods
Elm Hollow, NY 11854
email: MoonTotGoods@mailexample.test
tel.: (631) 555-0147
website: MoonTotGoods.example

Target Market(s)

18-40

Industry/Entity Type

Baby

Coding

Coded - Design and coding required

Number of Pages Required

5+ page

Requirements
Must have
• 1. Pages: Why buy from us, Contact Us, Home page, Products Page, Blog
• 2. Use the colors from our logo for the web design.
• 3. Need a link that will connect visitors to our facebook, instagram, Pinterest and Tumblr account. Would like links on,the top left side of the page
Nice to have
• My Cart page
• 1. On contact us page, we want to include some type of template for the customer to complete. (Ex: name, email address, contact number, optional home address, comments)
• 2. When clients visit our website, we want a capture/pop up for the customer to subscribe to our email list to receive discounts. (Ex. Want 10% off your next order ? Suscribe to our mailing list below and get a 10% off code to use at check out. If they don't want to subscribe, they have the option to select "No Thank You, I want to pay full price).
• 3. On home page have subscribe to our email list.

```html
<!DOCTYPE html>
<html lang="en">
<head>
<meta charset="utf-8">
<title>Moon Tot Goods – Baby Bibs</title>
<link rel="stylesheet" href="https://fonts.googleapis.com/css2?family=Mulish:wght@300;400;600;700&display=swap">
<style>
:root{
  --coral:#fc4b63;
  --lime:#eef520;
  --orange:#f9a11b;
  --teal:#1bb58f;
  --green:#8cc63f;
  --white:#ffffff;
  --ink:#333333;
  --muted:#666666;
  --card:#f9f9f9;
  --line:#e6e6e6;
}
*{box-sizing:border-box;margin:0;padding:0}
html,body{width:1200px;height:2844px;overflow:hidden}
body{font-family:"Mulish",Arial,sans-serif;color:var(--ink);background:var(--white);position:relative}
section,header,footer{position:absolute;left:0;width:1200px}
.abs{position:absolute}

/* Hero */
.hero{top:0;height:578px;background:linear-gradient(120deg,#c98b5a 0%,#e0a56f 40%,#e8b07a 70%,#d79e68 100%)}
.hero-photo{position:absolute;inset:0}
.nav{position:absolute;top:44px;left:0;width:1200px;display:flex;justify-content:center;align-items:center;gap:0}
.nav a{color:var(--white);text-decoration:none;font-size:15px;padding:0 11px}
.nav .active{background:var(--coral);width:66px;height:66px;border-radius:50%;display:flex;align-items:center;justify-content:center;margin-right:12px}
.nav .icon-btn{width:42px;height:42px;border-radius:50%;display:flex;align-items:center;justify-content:center;padding:0;margin-left:6px}
.nav .search{background:var(--green);margin-left:12px}
.nav .cart{background:var(--orange)}
.hero-badge{position:absolute;left:452px;top:165px;width:296px;height:296px;border-radius:50%;background:var(--white);display:flex;flex-direction:column;align-items:center;justify-content:center}
.brand-mark{font-weight:700;font-size:56px;color:var(--coral);letter-spacing:2px}
.hero-tag{font-size:33px;font-weight:400;color:#555;margin-top:6px}
.slider-arrows{position:absolute;top:500px;left:569px;display:flex;gap:8px}
.slider-arrows span{width:28px;height:28px;border-radius:50%;display:flex;align-items:center;justify-content:center}

/* About */
.about{top:578px;height:326px;background:var(--lime)}
.section-title{position:absolute;width:100%;text-align:center;font-size:26px;font-weight:400;letter-spacing:1px;color:var(--ink)}
.feature{position:absolute;top:120px;width:110px;margin-left:-55px;text-align:center}
.feature .dot{width:64px;height:64px;border-radius:50%;margin:0 auto;display:flex;align-items:center;justify-content:center}
.feature .shadow{width:54px;height:8px;border-radius:50%;margin:10px auto 0;background:rgba(0,0,0,.08)}
.feature p{font-size:12px;line-height:19px;margin-top:12px;color:#333}

/* Products */
.products{top:904px;height:973px;background:var(--white)}
.card{position:absolute;width:270px;height:362px;background:var(--card);box-shadow:0 2px 6px rgba(0,0,0,.1);text-align:center}
.card .bib{position:absolute;left:55px;top:38px;width:160px;height:190px;border-radius:40% 40% 46% 46%}
.card h3{position:absolute;top:257px;width:100%;font-size:15px;font-weight:400;color:#444}
.card p{position:absolute;top:287px;width:100%;font-size:12px;color:var(--muted)}
.card .btn{position:absolute;top:311px;left:91px;width:88px;height:28px;line-height:28px;font-size:10px;color:var(--white)}

/* Testimonials */
.testimonials{top:1877px;height:451px;background:var(--coral)}
.testimonials .section-title{color:var(--white);top:66px}
.dash{position:absolute;left:174px;width:852px;border-top:2px dashed rgba(255,255,255,.55)}
.t-arrow{position:absolute;top:66px;color:var(--white);font-size:24px}
.stamp{position:absolute;top:165px;width:182px;height:180px;background:var(--white);border:6px dotted var(--white);border-radius:6px;box-shadow:0 4px 10px rgba(0,0,0,.2);outline:4px dotted var(--white);outline-offset:2px}
.stamp .photo{position:absolute;left:16px;top:14px;width:138px;height:112px}
.stamp .name{position:absolute;top:136px;width:100%;text-align:center;font-size:11px;color:#3a8fd8}
.t-text{position:absolute;top:167px;width:192px;font-size:11px;line-height:19px;color:var(--white)}

/* Newsletter */
.newsletter{top:2328px;height:260px;background:var(--orange)}
.newsletter .section-title{color:var(--white);top:51px;font-size:26px}
.newsletter .lead{position:absolute;top:98px;width:100%;text-align:center;color:var(--white);font-size:15px;opacity:.85}
.subscribe{position:absolute;top:152px;left:248px;width:704px;height:57px;display:flex}
.subscribe .field{flex:1;background:var(--white);font-size:11px;color:#999;padding-left:18px;line-height:57px}
.subscribe .go{width:152px;background:var(--teal);color:var(--white);font-size:12px;text-align:center;line-height:57px;font-weight:600}

/* Footer */
.site-footer{top:2588px;height:256px;background:var(--white)}
.footer-brand{position:absolute;left:174px;top:64px;font-weight:700;font-size:40px;color:var(--coral);letter-spacing:2px}
.footer-links{position:absolute;left:377px;top:60px;list-style:none;font-size:12px;line-height:24px}
.footer-contact{position:absolute;left:605px;top:60px;font-size:12px;line-height:24px}
.social{position:absolute;left:842px;top:62px;display:flex;gap:6px}
.social span{width:30px;height:30px;border-radius:50%;border:1.5px solid #555}
.legal{position:absolute;top:199px;left:0;width:1200px;height:57px;border-top:1px solid var(--line);text-align:center;font-size:11px;line-height:57px;color:#444}
</style>
</head>
<body>

<header class="hero">
  <div class="hero-photo" role="img" aria-label="Photo of a smiling baby wearing a blue silicone bib"></div>
  <nav class="nav">
    <a class="active" href="#">Home</a>
    <a href="#">Products</a>
    <a href="#">Why Buy From Us</a>
    <a href="#">Blog</a>
    <a href="#">Contact Us</a>
    <a class="icon-btn search" href="#" aria-label="Search">
      <svg width="16" height="16" viewBox="0 0 16 16"><circle cx="6.5" cy="6.5" r="4.5" fill="none" stroke="#fff" stroke-width="2"/><line x1="10" y1="10" x2="14" y2="14" stroke="#fff" stroke-width="2.4" stroke-linecap="round"/></svg>
    </a>
    <a class="icon-btn cart" href="#" aria-label="Cart">
      <svg width="16" height="18" viewBox="0 0 16 18"><rect x="2" y="4" width="12" height="13" rx="1.5" fill="none" stroke="#fff" stroke-width="1.8"/><path d="M5 4 V3 a3 3 0 0 1 6 0 V4" fill="none" stroke="#fff" stroke-width="1.8"/></svg>
    </a>
  </nav>
  <div class="hero-badge">
    <div class="brand-mark">MTG</div>
    <div class="hero-tag">We sell baby bibs</div>
  </div>
  <div class="slider-arrows">
    <span style="background:#f3f3f3"><svg width="10" height="10" viewBox="0 0 10 10"><path d="M7 1 L3 5 L7 9" fill="none" stroke="#333" stroke-width="2"/></svg></span>
    <span style="background:#333"><svg width="10" height="10" viewBox="0 0 10 10"><path d="M3 1 L7 5 L3 9" fill="none" stroke="#fff" stroke-width="2"/></svg></span>
  </div>
</header>

<section class="about">
  <h2 class="section-title" style="top:48px">ABOUT SELL BABY BIBS</h2>
  <div class="feature" style="left:246px"><div class="dot" style="background:#f8555f"><svg width="30" height="30" viewBox="0 0 30 30"><circle cx="15" cy="15" r="11" fill="none" stroke="#fff" stroke-width="2"/><circle cx="15" cy="15" r="4" fill="none" stroke="#fff" stroke-width="2"/></svg></div><div class="shadow"></div><p>The bibs are made of 100% silicon</p></div>
  <div class="feature" style="left:362px"><div class="dot" style="background:#8cc63f"><svg width="28" height="30" viewBox="0 0 28 30"><path d="M14 3 L24 7 V15 C24 21 19 25 14 27 C9 25 4 21 4 15 V7 Z" fill="none" stroke="#fff" stroke-width="2"/><path d="M9 15 L13 19 L19 11" fill="none" stroke="#fff" stroke-width="2"/></svg></div><div class="shadow"></div><p>They are safe</p></div>
  <div class="feature" style="left:476px"><div class="dot" style="background:#1bc39b"><svg width="30" height="30" viewBox="0 0 30 30"><path d="M6 24 C10 12 18 7 25 5 C22 14 16 22 6 24 Z" fill="#fff"/></svg></div><div class="shadow"></div><p>Light Weight</p></div>
  <div class="feature" style="left:593px"><div class="dot" style="background:#1e9ad6"><svg width="30" height="30" viewBox="0 0 30 30"><path d="M12 25 V9 a2 2 0 0 1 4 0 V16 h6 a2 2 0 0 1 2 2 V25" fill="none" stroke="#fff" stroke-width="2"/></svg></div><div class="shadow"></div><p>Soft</p></div>
  <div class="feature" style="left:713px"><div class="dot" style="background:#9b27b0"><svg width="30" height="30" viewBox="0 0 30 30"><path d="M18 5 C24 10 22 22 12 25 C14 19 15 12 18 5 Z" fill="#fff"/></svg></div><div class="shadow"></div><p>Smooth</p></div>
  <div class="feature" style="left:834px"><div class="dot" style="background:#e0209a"><svg width="30" height="30" viewBox="0 0 30 30"><path d="M8 22 A8 8 0 1 1 22 22" fill="none" stroke="#fff" stroke-width="3"/></svg></div><div class="shadow"></div><p>Flexible</p></div>
  <div class="feature" style="left:952px"><div class="dot" style="background:#2dc653"><svg width="30" height="30" viewBox="0 0 30 30"><circle cx="15" cy="15" r="10" fill="none" stroke="#fff" stroke-width="2"/><circle cx="11.5" cy="12.5" r="1.3" fill="#fff"/><circle cx="18.5" cy="12.5" r="1.3" fill="#fff"/><path d="M10 17 Q15 22 20 17" fill="none" stroke="#fff" stroke-width="2"/></svg></div><div class="shadow"></div><p>Dishwasher Safe &amp; has funny faces.</p></div>
</section>

<section class="products">
  <h2 class="section-title" style="top:42px">OUR PRODUCTS</h2>
  <article class="card" style="left:174px;top:135px"><div class="bib" role="img" aria-label="Pink silicone baby bib with a funny face" style="background:linear-gradient(#f06fc0,#d81b8f)"></div><h3>MTG BABY BIBS</h3><p>At vero eos et accusamus et iusto</p><span class="btn" style="background:#e41fa0">ADD TO CART</span></article>
  <article class="card" style="left:466px;top:135px"><div class="bib" role="img" aria-label="Light blue silicone baby bib with a funny face" style="background:linear-gradient(#6cc6f2,#1f8fd6)"></div><h3>MTG BABY BIBS</h3><p>At vero eos et accusamus et iusto</p><span class="btn" style="background:#2ea6e6">ADD TO CART</span></article>
  <article class="card" style="left:756px;top:135px"><div class="bib" role="img" aria-label="Green silicone frog baby bib" style="background:linear-gradient(#a6d95a,#6ba52b)"></div><h3>MTG BABY BIBS</h3><p>At vero eos et accusamus et iusto</p><span class="btn" style="background:#7db83a">ADD TO CART</span></article>
  <article class="card" style="left:174px;top:516px"><div class="bib" role="img" aria-label="Orange silicone tiger baby bib" style="background:linear-gradient(#fbbf3a,#f08a10)"></div><h3>MTG BABY BIBS</h3><p>At vero eos et accusamus et iusto</p><span class="btn" style="background:#f7961c">ADD TO CART</span></article>
  <article class="card" style="left:466px;top:516px"><div class="bib" role="img" aria-label="Blue silicone shark baby bib" style="background:linear-gradient(#4aa6ec,#1c5fc9)"></div><h3>MTG BABY BIBS</h3><p>At vero eos et accusamus et iusto</p><span class="btn" style="background:#1e6fd6">ADD TO CART</span></article>
  <article class="card" style="left:756px;top:516px"><div class="bib" role="img" aria-label="Yellow silicone frog baby bib" style="background:linear-gradient(#eef05a,#c9d21a)"></div><h3>MTG BABY BIBS</h3><p>At vero eos et accusamus et iusto</p><span class="btn" style="background:#cfd41a">ADD TO CART</span></article>
</section>

<section class="testimonials">
  <span class="t-arrow" style="left:172px">&#8249;</span>
  <h2 class="section-title">TESTIMONIALS</h2>
  <span class="t-arrow" style="left:1005px">&#8250;</span>
  <div class="dash" style="top:123px"></div>
  <div class="stamp" style="left:184px"><div class="photo" role="img" aria-label="Portrait of a customer" style="background:linear-gradient(#c9b8a6,#8a7462)"></div><div class="name">CLARA DUNN</div></div>
  <p class="t-text" style="left:390px">Sed ut perspiciatis unde omnis iste natus error sit voluptatem accusantium doloremque laudantium, totam rem aperiam, eaque ipsa quae ab illo inventore veritatis et quasi architecto beatae vitae dicta sunt explicabo. Nemo enim ipsam voluptatem quia</p>
  <div class="stamp" style="left:612px"><div class="photo" role="img" aria-label="Portrait of a customer" style="background:linear-gradient(#8fa0ad,#c9a24a)"></div><div class="name">CLARA DUNN</div></div>
  <p class="t-text" style="left:815px">Sed ut perspiciatis unde omnis iste natus error sit voluptatem accusantium doloremque laudantium, totam rem aperiam, eaque ipsa quae ab illo inventore veritatis et quasi architecto beatae vitae dicta sunt explicabo. Nemo enim ipsam voluptatem quia</p>
  <div class="dash" style="top:392px"></div>
</section>

<section class="newsletter">
  <h2 class="section-title">NEWSLETTER SUBSCRIPTION</h2>
  <p class="lead">Sed ut perspiciatis unde omnis iste natus error sit voluptatem accusantium</p>
  <div class="subscribe"><div class="field">Enter Your E-mail Address</div><div class="go">SUBSCRIBE NOW</div></div>
</section>

<footer class="site-footer">
  <div class="footer-brand">MTG</div>
  <ul class="footer-links"><li>Home</li><li>Products</li><li>Why Buy From Us</li><li>Blog</li><li>Contact Us</li></ul>
  <div class="footer-contact">Moon Tot Goods<br>Elm Hollow, NY 11854<br><br>E-mail: MoonTotGoods@mailexample.test<br>Tel.: (631) 555-0147</div>
  <div class="social" aria-label="Social links"><span></span><span></span><span></span><span></span></div>
  <div class="legal">© 2016 Company Name | All Rights Reserved</div>
</footer>

</body>
</html>
```